Simply recommend a shopify theme that will best suit our business

FIRSTLY, To avoid a shotgun approach to submissions and to ensure contestants actually put THOUGHT to their submission and its qualification of our requirements below, EACH CONTESTANT MAY ONLY SUBMIT 3 SELECTIONS. IF YOU SUBMIT MORE YOUR ENTIRE SET WILL BE DELETED AND YOU WILL BE REMOVED FROM THE CONTEST.

[login to view URL] will be our new home. You can see [login to view URL] we are preparing our consumer market purchasing wellness and nutritional supplements online for our new business model.
We would like our new e-com site to cater to showcasing our supplements with a strong sorting function i.e. by brand, ailment, tag etc. Responsive, interactive, mobile-centric, e-com focused with an ability to catalogue many products. Customers must be able to create a profile that remembers their orders and delivery address and give them the opportunity to select repeat order and date of requested delivery and frequency etc.

We would like to run a contest to see which freelancer recommends the Shopify theme that best suits our needs accordingly. You may always look at what other companies with a similar function are using.

These are some of the requirements we have of the theme: (as many of them as possible)

TRIAL OPTION TO QUALIFY THEME
MUST BE MOBILE CENTRIC
ACCESS TO YOUTUBE AND SOCIAL MEDIA
PRODUCT GROUPING BY AILMENT, BRAND,
SUBSCRIBE TO NEWSLETTER
SLIDERS, HEADER SLIDE SHOW
LOG IN
REGISTER
AI READY, LIVE CHAT READY
DOWNLOADABLE PDF - DETAILED PRODUCT INFO
SIZE CHOICES ON A PRODUCT LINE
SORT BY CATEGORY / KEYWORD / ASSORTED PACK / BRAND
SHARE TO SOCIAL MEDIA
COUPON CODE
DRIVE CONVERSIONS WHEREVER THE CUSTOMER IS
FAST CHECK OUT / CART AND ADD TO CART
PROMOTE SPECIALS, DISCOUNTS, GROUPING, FEATURED, NEW PRODUCT DISPLAYS
HOME PAGE VIDEO
MULTI COLUM DROP DOWN MENU - MOBILE CENTRIC
FULL-WIDTH LAYOUT
FREE STOCK PHOTOS
SUPPORT / UPGRADES
SEARCH ENGINE OPTIMISED
FAST LOADING SPEED
MAGAZINE TYPE INSTAGRAM / FACEBOOK FEED INTEGRATION OR BLOG TO SOCIAL MEDIA
INTEGRATION CAPABILITY TO OTHER APPS SUCH AS UNLEASHED, BILLDOZER, XERO ETC

PLEASE ENSURE TO SUBMIT THE LINK AND THE SCREENSHOT OF THE HOMEPAGE FOR EACH SUBMISSION.

A FREELANCER THAT SUBMITS A THEME FIRST HAS RIGHT TO THAT SUBMISSION IF DUPLICATES ARE SUBMITTED BY ANOTHER FREELANCER.

Also, preview the submissions of the other contestants as mentioned to ensure you don't waste a submission on an already submitted theme.

```html
<!DOCTYPE html>
<html lang="en">
<head>
<meta charset="utf-8">
<title>Verdela Theme Promo</title>
<link rel="stylesheet" href="https://fonts.googleapis.com/css2?family=Poppins:wght@400;500;600;700&display=swap">
<style>
:root{
  --bg:#2e2e2e;
  --card:#ffffff;
  --ink:#222222;
  --muted:#8a8a8a;
  --line:#ececec;
  --green:#6dbe2c;
  --green-dark:#55a01c;
  --red:#e9424b;
  --star:#f2b01e;
  --soft:#f4f6f2;
}
*{box-sizing:border-box;margin:0;padding:0}
html,body{width:1200px;height:610px;overflow:hidden;background:var(--bg);font-family:"Poppins",sans-serif;color:var(--ink)}
.banner{position:relative;width:1200px;height:610px;overflow:hidden;background:var(--bg)}
.card{position:absolute;background:var(--card);box-shadow:0 8px 24px rgba(0,0,0,.35);overflow:hidden}
.media{position:absolute}
.brand{font-weight:700;font-size:11px;color:var(--ink);display:flex;align-items:center;gap:4px}
.brand i{display:inline-block;width:7px;height:7px;background:var(--green);border-radius:50%}
.nav{position:absolute;left:0;right:0;height:14px;background:var(--green);display:flex;gap:14px;align-items:center;padding-left:40px;font-size:6px;color:#fff;text-transform:uppercase}
.hero-title{font-weight:700;line-height:1.2}
.stars{display:flex;gap:2px}
.stars span{width:9px;height:9px;background:var(--star);clip-path:polygon(50% 0,61% 35%,98% 35%,68% 57%,79% 91%,50% 70%,21% 91%,32% 57%,2% 35%,39% 35%)}
.stars span.off{background:#d9d9d9}
.price{font-weight:700}
.btn{display:inline-block;background:var(--green);color:#fff;font-size:6px;font-weight:600;padding:4px 10px;border-radius:2px;text-transform:uppercase}
.grid{position:absolute;display:flex;gap:8px}
.grid .item{width:34px;height:48px;border-radius:2px}
.badge{position:absolute;left:942px;top:-104px;width:330px;height:330px;border-radius:50%;background:var(--red);color:#fff;text-align:center}
.badge .off{position:absolute;left:0;right:0;top:122px;font-size:58px;font-weight:600;letter-spacing:-1px;padding-right:60px}
.badge .until{position:absolute;left:0;right:0;top:196px;font-size:19px;font-weight:600;padding-right:60px}
.app-tile{position:absolute;left:508px;top:220px;width:102px;height:102px;border-radius:22px;background:var(--green);display:flex;align-items:center;justify-content:center;color:#fff;font-weight:600;font-size:17px}
</style>
</head>
<body>
<main class="banner">

  <!-- home page preview, top left -->
  <section class="card" style="left:0;top:0;width:315px;height:325px">
    <div class="brand" style="position:absolute;left:30px;top:8px"><i></i>VERDELA</div>
    <div class="nav" style="top:26px"><span>Home</span><span>Shop</span><span>Blog</span><span>Pages</span><span>Contact</span></div>
    <div class="media" role="img" aria-label="Woman with skincare leaf, hero photo" style="left:0;top:40px;width:315px;height:120px;background:linear-gradient(90deg,#f3f1ec 40%,#d9c3ab 70%,#7fae4a)"></div>
    <div class="hero-title" style="position:absolute;left:18px;top:80px;font-size:15px">The Sale 70%<br>On All New Products</div>
    <div style="position:absolute;left:0;right:0;top:190px;text-align:center;font-size:7px;font-weight:600">Our Product</div>
    <div style="position:absolute;left:0;right:0;top:204px;display:flex;justify-content:center;gap:12px;font-size:5px;color:var(--muted);text-transform:uppercase"><span style="color:var(--green)">Skin</span><span>Hair</span><span>Body</span><span>Oils</span><span>Sets</span></div>
    <div class="stars" style="position:absolute;left:36px;top:252px"><span></span><span></span><span class="off"></span><span class="off"></span><span class="off"></span></div>
    <div class="price" style="position:absolute;left:36px;top:275px;font-size:19px">$25.00</div>
  </section>

  <!-- single product tile, top center -->
  <section class="card" style="left:366px;top:0;width:233px;height:86px">
    <div class="media" role="img" aria-label="Lavender serum bottle" style="left:80px;top:0;width:70px;height:60px;background:linear-gradient(180deg,#d8c9dc,#b7a3c0)"></div>
    <div class="stars" style="position:absolute;left:92px;top:68px"><span></span><span></span><span class="off"></span><span class="off"></span><span class="off"></span></div>
  </section>

  <!-- tall collection card -->
  <section class="card" style="left:335px;top:122px;width:116px;height:280px">
    <div class="media" role="img" aria-label="Jar of cream and cream swatch" style="left:0;top:0;width:116px;height:120px;background:radial-gradient(circle at 50% 55%,#f0d796,#e2c27a 35%,#f5f3ee 60%)"></div>
    <div class="hero-title" style="position:absolute;left:12px;top:150px;font-size:9px">New Collection<br>Winter '19</div>
    <div class="media" role="img" aria-label="Green leaves" style="left:60px;top:190px;width:56px;height:90px;background:linear-gradient(135deg,#f7f7f5,#8fbf5a 70%)"></div>
  </section>

  <!-- collection banner, bottom left -->
  <section class="card" style="left:0;top:376px;width:335px;height:142px">
    <div class="media" role="img" aria-label="Dropper bottles on green background" style="left:210px;top:0;width:125px;height:142px;background:linear-gradient(135deg,#e9f2dd,#9fcf6a 60%,#6aa63a)"></div>
    <div class="hero-title" style="position:absolute;left:10px;top:38px;font-size:20px">New Collection Winter '19</div>
    <span class="btn" style="position:absolute;left:18px;top:90px">Shop Now</span>
  </section>

  <!-- sale hero, bottom center -->
  <section class="card" style="left:234px;top:498px;width:341px;height:112px">
    <div class="media" role="img" aria-label="White cosmetic bottles with cotton" style="left:150px;top:0;width:191px;height:80px;background:linear-gradient(90deg,#f4f4f2,#d9dcd6)"></div>
    <div class="hero-title" style="position:absolute;left:30px;top:26px;font-size:12px">The Sale 70%<br>On All New Products</div>
    <div class="grid" style="left:30px;top:90px"><div class="item" style="background:var(--soft)"></div><div class="item" style="background:var(--soft)"></div><div class="item" style="background:var(--soft)"></div><div class="item" style="background:var(--soft)"></div></div>
  </section>

  <!-- brand tile -->
  <div class="app-tile">Verdela</div>

  <!-- promo strip, top right -->
  <section class="card" style="left:706px;top:51px;width:290px;height:101px">
    <div style="position:absolute;left:14px;top:22px;width:150px;font-size:9.5px;font-weight:500;line-height:1.45">Awesome total sale - 50% off for oil cosmetics Verdela!</div>
    <div class="media" role="img" aria-label="Blue and white cosmetic bottles" style="left:180px;top:0;width:110px;height:101px;background:linear-gradient(180deg,#dbe9f2,#f4f7f9)"></div>
  </section>

  <!-- shop listing, right -->
  <section class="card" style="left:843px;top:91px;width:357px;height:244px">
    <div class="brand" style="position:absolute;left:16px;top:10px"><i></i>VERDELA</div>
    <div class="nav" style="top:28px;padding-left:30px"><span>Home</span><span>Shop</span><span>Blog</span><span>Pages</span><span>Contact</span></div>
    <div style="position:absolute;left:20px;top:60px;font-size:7px;font-weight:600">Best Sellers</div>
    <div class="grid" style="left:20px;top:76px;gap:12px">
      <div class="item" role="img" aria-label="Product bottle" style="background:linear-gradient(#f1e9ef,#d9c3cf)"></div>
      <div class="item" role="img" aria-label="Product bottle" style="background:linear-gradient(#eef1ea,#d4dbc9)"></div>
      <div class="item" role="img" aria-label="Product bottle" style="background:linear-gradient(#f3ecdf,#dfcfb3)"></div>
      <div class="item" role="img" aria-label="Product bottle" style="background:linear-gradient(#f1e9ef,#d9c3cf)"></div>
      <div class="item" role="img" aria-label="Product bottle" style="background:linear-gradient(#eef1ea,#d4dbc9)"></div>
      <div class="item" role="img" aria-label="Product bottle" style="background:linear-gradient(#f3ecdf,#dfcfb3)"></div>
    </div>
  </section>

  <!-- single product, right -->
  <section class="card" style="left:752px;top:203px;width:98px;height:134px">
    <div class="media" role="img" aria-label="Green skincare tube" style="left:30px;top:10px;width:38px;height:56px;background:linear-gradient(180deg,#7fbf3f,#f1f4ec)"></div>
    <div class="stars" style="position:absolute;left:14px;top:76px"><span></span><span></span><span class="off"></span><span class="off"></span><span class="off"></span></div>
    <div class="price" style="position:absolute;left:12px;top:96px;font-size:17px">$25.00</div>
  </section>

  <!-- sale hero, bottom right -->
  <section class="card" style="left:792px;top:355px;width:408px;height:255px">
    <div class="brand" style="position:absolute;left:20px;top:8px"><i></i>VERDELA</div>
    <div class="nav" style="top:24px;padding-left:30px"><span>Home</span><span>Shop</span><span>Blog</span><span>Pages</span><span>Contact</span></div>
    <div class="media" role="img" aria-label="Row of amber and white cosmetic bottles" style="left:0;top:38px;width:408px;height:217px;background:linear-gradient(90deg,#9b8a74 0%,#5f5347 45%,#3f372f)"></div>
    <div class="hero-title" style="position:absolute;left:40px;top:90px;font-size:20px;color:#fff">The Sale 70%<br>On All New Products</div>
  </section>

  <!-- mini listing, bottom -->
  <section class="card" style="left:710px;top:528px;width:124px;height:82px">
    <div class="grid" style="left:10px;top:14px;gap:6px">
      <div class="item" role="img" aria-label="Product bottle" style="width:30px;background:linear-gradient(#f3ecdf,#dfcfb3)"></div>
      <div class="item" role="img" aria-label="Product bottle" style="width:30px;background:linear-gradient(#eef1ea,#d4dbc9)"></div>
      <div class="item" role="img" aria-label="Product bottle" style="width:30px;background:linear-gradient(#f1e9ef,#d9c3cf)"></div>
    </div>
  </section>

  <!-- discount badge -->
  <div class="badge">
    <div class="off">-30%</div>
    <div class="until">UNTIL 17 JULY</div>
  </div>

</main>
</body>
</html>
```